Briefpapier für IT-Dienstleister
Zielgruppe
Hallo wir sind IT Dienstleister und Verkaufen viel Hard- und Software, jedoch liegt der Fokus auf IT-Security und Netzwerkaustattung.
Die Zielgruppe sind ausschliesslich Geschäftskunden aus Klein und Großunternehmen.
New Homepage(name): https://velor-netz.de
Old homepage(name): https://kornwerk.de
Aufgabenstellung
Das Briefpapier soll den Namen und unser Logo 'velor IT netz' behinhalten.
Homepage: https://www.velor-netz.de
main name = velor IT netz
Die Firmenadresse(Footer) bleibt jedoch gleich: Kornwerk Elektrotechnik GmbH & Co. Vertriebs KG

```html
<!DOCTYPE html>
<html lang="de">
<head>
<meta charset="utf-8">
<title>velor IT netz – Geschäftsausstattung</title>
<link href="https://fonts.googleapis.com/css2?family=Exo+2:wght@400;600&family=Nunito+Sans:wght@400;600&display=swap" rel="stylesheet">
<style>
:root{
  --bg:#e3e3e6;
  --paper:#f4f5f6;
  --ink:#1e1e1e;
  --text:#4a4a4a;
  --muted:#777;
  --orange:#f7914d;
  --square:#e2e2e3;
  --dark:#232324;
  --dark2:#323235;
  --brand-font:"Exo 2",sans-serif;
  --body-font:"Nunito Sans",sans-serif;
}
*{box-sizing:border-box;margin:0;padding:0}
html,body{width:1181px;height:1200px;overflow:hidden}
body{background:var(--bg);font-family:var(--body-font);color:var(--text);position:relative}
.sheet{position:absolute;width:296px;height:420px;background:var(--paper)}
.sq{position:absolute;background:var(--square)}
.brand{position:absolute;z-index:2;display:flex;align-items:center;gap:4px;font-family:var(--brand-font);font-weight:600;color:var(--ink);white-space:nowrap;letter-spacing:-.2px}
.brand .mark{display:inline-block;background:var(--orange)}
.brand-lg{font-size:13px}.brand-lg .mark{width:7px;height:7px}
.brand-sm{font-size:6px;gap:2px}.brand-sm .mark{width:4px;height:4px}
.brand-md{font-size:8px;gap:3px}.brand-md .mark{width:5px;height:5px}
.brand-light{color:#fff}
.body-copy{position:absolute;width:164px;font-size:6.5px;line-height:7.6px;letter-spacing:.4px;text-align:justify;color:var(--text)}
.body-copy p+p{margin-top:7px}
.body-copy strong{font-weight:600;color:var(--ink)}
.date{position:absolute;font-size:6.6px;letter-spacing:.4px}
.small{font-size:4.4px;line-height:6.8px;letter-spacing:.3px;color:var(--muted)}
.rule{position:absolute;height:1px;background:#888}
.accent-bar{position:absolute;background:var(--orange)}
.footer-line{position:absolute;font-size:6px;letter-spacing:.35px;color:var(--muted);white-space:nowrap}
.footer-line .sep{color:var(--orange);margin:0 3px}
.block{position:absolute}
.dark{position:absolute;background:linear-gradient(180deg,var(--dark),var(--dark2))}
.dsq{position:absolute;background:linear-gradient(135deg,#1c1c1d,#3d3d40);border-left:1px solid #555}
.envelope{position:absolute;left:391px;top:955px;width:331px;height:166px;background:var(--paper)}
.flap{position:absolute;left:0;top:0;width:331px;height:44px;z-index:1}
</style>
</head>
<body>

<!-- Letter with accent bar -->
<section class="sheet" style="left:100px;top:60px">
  <div class="sq" style="left:30px;top:26px;width:26px;height:26px"></div>
  <div class="sq" style="left:64px;top:40px;width:14px;height:14px"></div>
  <div class="sq" style="left:98px;top:22px;width:18px;height:18px"></div>
  <div class="sq" style="left:18px;top:96px;width:16px;height:16px"></div>
  <div class="sq" style="left:44px;top:100px;width:28px;height:28px"></div>
  <div class="sq" style="left:84px;top:112px;width:12px;height:12px"></div>
  <div class="sq" style="left:22px;top:140px;width:20px;height:20px"></div>
  <div class="sq" style="left:52px;top:146px;width:14px;height:22px"></div>
  <div class="sq" style="left:26px;top:206px;width:18px;height:18px"></div>
  <div class="brand brand-lg" style="left:53px;top:64px">velor <span class="mark"></span> IT netz</div>
  <div class="accent-bar" style="left:0;top:175px;width:57px;height:17px"></div>
  <div class="body-copy" style="left:71px;top:174px">
    <p>Sep 27, 2019 (HKR Market <strong>Intelligence via CORATEX) -- A new market study</strong> on Global Pet Medicine Market with 100+ market data Tables, Pie Chart &amp; Graphs is released that will provide complete assessment of the Market and covers evolving trends, current scenario analysis and growth factors, and industry validated market data. The research study provides market breakdown by re</p>
    <p>venue and volume (if applicable) and price history estimates for Global Pet Medicine. Some are the key players from the coverage that are also part of the study are Halden Ingwerk, Zorvet, Marlo, Elvano, Baulen, Virdan, Cerin Sante Animale, Vetomarin, Bivera Animal Health &amp; Dorvan Pharmaceuticals. Get ready to identify the pros and cons of regulatory framework of the Indus</p>
  </div>
  <div class="rule" style="left:22px;top:389px;width:258px"></div>
  <div class="footer-line" style="left:22px;top:393px">Lindenstr.12 .D: 2208<span class="sep">|</span>Postfach: 38127064<span class="sep">|</span>Fon: 30418856<span class="sep">|</span>Fax: 7315092</div>
</section>

<!-- Blank letter, right footer -->
<section class="sheet" style="left:427px;top:60px">
  <div class="sq" style="left:40px;top:24px;width:26px;height:26px"></div>
  <div class="sq" style="left:74px;top:38px;width:14px;height:14px"></div>
  <div class="sq" style="left:108px;top:20px;width:18px;height:18px"></div>
  <div class="sq" style="left:28px;top:94px;width:16px;height:16px"></div>
  <div class="sq" style="left:54px;top:98px;width:28px;height:28px"></div>
  <div class="sq" style="left:94px;top:110px;width:12px;height:12px"></div>
  <div class="sq" style="left:32px;top:138px;width:20px;height:20px"></div>
  <div class="sq" style="left:62px;top:144px;width:14px;height:22px"></div>
  <div class="sq" style="left:36px;top:204px;width:18px;height:18px"></div>
  <div class="brand brand-lg" style="left:65px;top:61px">velor <span class="mark"></span> IT netz</div>
  <div class="block" style="right:27px;top:353px;text-align:right">
    <div class="brand brand-sm" style="position:static;justify-content:flex-end">velor <span class="mark"></span> IT netz</div>
    <div class="small" style="margin-top:3px">Lindenstr.12 .D: 2208<br>Postfach: 38127064<br>Fon: 30418856<br>Fax: 7315092<br>Email: 001880017400126</div>
  </div>
</section>

<!-- Letter with full footer -->
<section class="sheet" style="left:95px;top:506px">
  <div class="sq" style="left:38px;top:26px;width:26px;height:26px"></div>
  <div class="sq" style="left:72px;top:40px;width:14px;height:14px"></div>
  <div class="sq" style="left:106px;top:22px;width:18px;height:18px"></div>
  <div class="sq" style="left:26px;top:96px;width:16px;height:16px"></div>
  <div class="sq" style="left:52px;top:100px;width:28px;height:28px"></div>
  <div class="sq" style="left:92px;top:112px;width:12px;height:12px"></div>
  <div class="sq" style="left:30px;top:140px;width:20px;height:20px"></div>
  <div class="sq" style="left:60px;top:146px;width:14px;height:22px"></div>
  <div class="sq" style="left:34px;top:206px;width:18px;height:18px"></div>
  <div class="brand brand-lg" style="left:62px;top:62px">velor <span class="mark"></span> IT netz</div>
  <div class="rule" style="left:17px;top:347px;width:90px"></div>
  <div class="brand brand-md" style="left:113px;top:342px">velor <span class="mark"></span> IT netz</div>
  <div class="rule" style="left:185px;top:347px;width:90px"></div>
  <div class="block small" style="left:19px;top:356px">
    <div class="brand brand-sm" style="position:static;margin-bottom:2px">velor <span class="mark"></span> IT netz</div>
    Lindenstr.12 .D: 2208<br>Postfach: 38127064<br>Fon: 30418856<br>Fax: 7315092<br>Email: 001880017400126
  </div>
  <div class="block small" style="left:112px;top:360px;width:84px">Handelsregister HRA 47215<br>Persönlich haftende Gesellschaft:<br>Kornwerk Elektrotechnik<br>GmbH &amp; Co. Vertriebs KG +<br>Vertrieb von Elektronik &amp;<br>Lichttechnik</div>
  <div class="block small" style="left:206px;top:360px">Bankverbindung: Stadtbanc<br>Frankfurt<br>IBAN: DE12 3004 0071<br>SWIFT / BIC : STBKDEFF<br>Ust-Idnr: 804219367</div>
  <div class="footer-line" style="left:17px;top:405px;font-size:5px;color:var(--ink)">Kornwerk Elektrotechnik GmbH &amp; Co. Vertriebs KG + Vertrieb von Elektronik &amp; Lichttechnik</div>
</section>

<!-- Letter with sender and signature -->
<section class="sheet" style="left:426px;top:506px">
  <div class="sq" style="left:36px;top:30px;width:26px;height:26px"></div>
  <div class="sq" style="left:70px;top:44px;width:14px;height:14px"></div>
  <div class="sq" style="left:104px;top:26px;width:18px;height:18px"></div>
  <div class="sq" style="left:22px;top:94px;width:16px;height:16px"></div>
  <div class="sq" style="left:50px;top:98px;width:24px;height:24px"></div>
  <div class="sq" style="left:80px;top:106px;width:12px;height:12px"></div>
  <div class="sq" style="left:34px;top:176px;width:20px;height:20px"></div>
  <div class="sq" style="left:64px;top:184px;width:14px;height:22px"></div>
  <div class="sq" style="left:30px;top:230px;width:18px;height:18px"></div>
  <div class="brand brand-lg" style="left:60px;top:68px">velor <span class="mark"></span> IT netz</div>
  <div class="date" style="left:103px;top:121px">Sep 27, 2019</div>
  <div class="block" style="left:32px;top:146px">
    <div style="font-size:7px;font-weight:600;color:var(--ink);letter-spacing:.4px">MAREIKE</div>
    <div style="font-size:6.4px;letter-spacing:.4px;color:var(--muted);margin-top:1px">Directrice</div>
  </div>
  <div class="body-copy" style="left:102px;top:146px">
    <p>Sep 27, 2019 (HKR Market <strong>Intelligence via CORATEX) -- A new market study</strong> on Global Pet Medicine Market with 100+ market data Tables, Pie Chart &amp; Graphs is released that will provide complete assessment of the Market and covers evolving trends, current scenario analysis and growth factors, and industry validated market data. The research study provides market breakdown by re</p>
    <p>venue and volume (if applicable) and price history estimates for Global Pet Medicine. Some are the key players from the coverage that are also part of the study are Halden Ingwerk, Zorvet, Marlo, Elvano, Baulen, Virdan, Cerin Sante Animale, Vetomarin, Bivera Animal Health &amp; Dorvan Pharmaceuticals. Get ready to identify the pros and cons of regulatory framework of the Indus</p>
  </div>
  <div class="block small" style="left:16px;top:307px">
    <div class="brand brand-sm" style="position:static;margin-bottom:2px">velor <span class="mark"></span> IT netz</div>
    Lindenstr.12 .D: 2208<br>Postfach: 38127064<br>Fon: 30418856<br>Fax: 7315092<br>Email: 001880017400126
    <div style="width:58px;height:1px;background:#888;margin:4px 0"></div>
    Bankverbindung: Stadtbanc<br>Frankfurt<br>IBAN: DE12 3004 0071<br>SWIFT / BIC: STBKDEFF<br>Ust-Idnr: 804219367
  </div>
  <div class="block" style="right:30px;top:322px;font-size:7px;font-weight:600;color:var(--ink);letter-spacing:.4px">SIGNATURE</div>
  <div class="rule" style="left:102px;top:381px;width:173px"></div>
  <div class="block small" style="left:102px;top:384px;width:173px;text-align:center;font-size:3.8px;line-height:6.4px">Handelsregister HRA 47215 Persönlich haftende Gesellschaft: Kornwerk Elektrotechnik GmbH &amp; Co. Vertriebs KG + Vertrieb von Elektronik &amp; Lichttechnik</div>
</section>

<!-- Business card -->
<section class="dark" style="left:776px;top:474px;width:334px;height:169px">
  <div class="brand brand-light" style="right:24px;top:34px;font-size:14px;gap:4px">velor <span class="mark" style="width:7px;height:7px"></span> IT netz</div>
  <div class="dsq" style="left:26px;top:92px;width:18px;height:18px"></div>
  <div class="dsq" style="left:54px;top:84px;width:12px;height:12px"></div>
  <div class="dsq" style="left:58px;top:112px;width:24px;height:24px"></div>
  <div class="dsq" style="left:94px;top:98px;width:14px;height:14px"></div>
  <div class="dsq" style="left:30px;top:128px;width:14px;height:14px"></div>
  <div class="dsq" style="left:118px;top:122px;width:18px;height:18px"></div>
  <div class="dsq" style="left:148px;top:104px;width:10px;height:10px"></div>
  <div class="block" style="right:24px;top:130px;text-align:right;font-size:5.4px;line-height:6.6px;color:#fff;letter-spacing:.2px">(555) 014-2287<br>info@velor-netz.de<br>12 Lindenstraße, 60311 Frankfurt</div>
</section>

<!-- Folder -->
<section class="dark" style="left:777px;top:657px;width:334px;height:444px">
  <div class="dsq" style="left:44px;top:50px;width:32px;height:32px"></div>
  <div class="dsq" style="left:90px;top:66px;width:18px;height:18px"></div>
  <div class="dsq" style="left:134px;top:42px;width:24px;height:24px"></div>
  <div class="dsq" style="left:30px;top:136px;width:22px;height:22px"></div>
  <div class="dsq" style="left:64px;top:142px;width:38px;height:38px"></div>
  <div class="dsq" style="left:118px;top:156px;width:16px;height:16px"></div>
  <div class="dsq" style="left:36px;top:198px;width:26px;height:26px"></div>
  <div class="dsq" style="left:76px;top:206px;width:18px;height:30px"></div>
  <div class="dsq" style="left:42px;top:284px;width:24px;height:24px"></div>
  <div class="brand brand-light" style="left:106px;top:349px;font-size:16px;gap:5px">velor <span class="mark" style="width:8px;height:8px"></span> IT netz</div>
</section>

<!-- Envelope -->
<section class="envelope">
  <svg class="flap" viewBox="0 0 331 44" aria-hidden="true">
    <path d="M0 0H331L327 33Q325 44 313 44H18Q6 44 4 33Z" fill="#262627"/>
  </svg>
  <div class="brand brand-light" style="left:108px;top:18px;font-size:13px">velor <span class="mark"></span> IT netz</div>
  <div class="sq" style="left:22px;top:88px;width:18px;height:18px"></div>
  <div class="sq" style="left:50px;top:80px;width:12px;height:12px"></div>
  <div class="sq" style="left:54px;top:112px;width:24px;height:24px"></div>
  <div class="sq" style="left:90px;top:96px;width:14px;height:14px"></div>
  <div class="sq" style="left:26px;top:124px;width:14px;height:14px"></div>
  <div class="sq" style="left:114px;top:120px;width:18px;height:18px"></div>
  <div class="sq" style="left:144px;top:102px;width:10px;height:10px"></div>
  <div class="sq" style="left:164px;top:128px;width:14px;height:14px"></div>
</section>

</body>
</html>
```